Corvatel Website Graphic design

we want a replacement of existing designs in our existing website.. we want you to suggest and create a better graphical designs which suits our service with good representation explaining our process and services
Website Url: https://corvatelq.example
Basic Requirements -
1. Flat architecture
2. A good color palette
3. Icons to support the Content
4. Consistent Images in alignment with the Business
5. Use white space to let the Content breathe

Target Market(s)

Manufacturers & E-Commerce Distributors

Industry/Entity Type

Data Service

Colors

Designer to choose colors to be used in the design.

Requirements
Must have
• Creativity and originality
Nice to have
• Try to keep it Simple

```html
<!DOCTYPE html>
<html lang="en">
<head>
<meta charset="utf-8">
<title>Corvatel Solutions</title>
<link rel="stylesheet" href="https://fonts.googleapis.com/css2?family=Nunito+Sans:wght@300;400;600&family=Open+Sans:wght@600;700&display=swap">
<style>
  :root {
    --ink: #111111;
    --nav-grey: #6f6f6f;
    --hero-violet: #7476b0;
    --hero-violet-deep: #6a6bab;
    --band-violet: #66669c;
    --white: #ffffff;
    --panel-grey: #eee8e8;
    --cart-dark: #3a3b3d;
    --cart-orange: #e99544;
    --db-green: #7bbd42;
    --gear-violet: #7479b8;
  }
  * { box-sizing: border-box; margin: 0; padding: 0; }
  html, body { width: 1000px; height: 1200px; overflow: hidden; background: var(--white); }
  body { position: relative; font-family: "Nunito Sans", Arial, sans-serif; color: var(--ink); }

  .site-header { position: absolute; left: 0; top: 0; width: 1000px; height: 110px; }
  .brand { position: absolute; left: 88px; top: 34px; display: flex; align-items: center; gap: 10px; }
  .brand-mark { width: 14px; height: 14px; border-radius: 50%; background: var(--hero-violet); }
  .brand-name { font-size: 24px; line-height: 1.05; font-weight: 600; color: var(--ink); }
  .main-nav { position: absolute; right: 66px; top: 66px; display: flex; gap: 22px; }
  .main-nav a { font-size: 18px; font-weight: 300; color: var(--nav-grey); text-decoration: none; letter-spacing: 0.3px; }

  .hero { position: absolute; left: 54px; top: 111px; width: 892px; height: 445px;
    box-shadow: 0 4px 14px rgba(0,0,0,0.12); overflow: hidden; }
  .hero-backdrop { position: absolute; inset: 0;
    background: radial-gradient(ellipse at 30% 40%, #7c7fbf 0%, var(--hero-violet) 45%, var(--hero-violet-deep) 100%); }
  .hero-title { position: absolute; left: 0; right: 0; top: 50px; text-align: center; color: var(--white);
    font-family: "Open Sans", Arial, sans-serif; font-weight: 600; font-size: 60px; line-height: 68px; }
  .hero-title .line-one { letter-spacing: 7px; display: block; }
  .hero-title .line-two { letter-spacing: 1px; display: block; }
  .hero-band { position: absolute; left: 0; right: 0; top: 262px; height: 114px; background: var(--band-violet);
    display: flex; flex-direction: column; justify-content: center; align-items: center; }
  .hero-band p { color: var(--white); font-size: 17.5px; font-weight: 600; line-height: 25.5px; text-align: center; }

  .feature-heading { position: absolute; font-family: "Open Sans", Arial, sans-serif; font-weight: 700;
    font-size: 26px; letter-spacing: 0.3px; color: var(--ink); }
  .feature-panel { position: absolute; background: var(--panel-grey); }
  .feature-panel p { font-size: 19px; line-height: 27px; color: var(--ink); letter-spacing: 0.2px; }

  .ecommerce-heading { left: 145px; top: 622px; }
  .ecommerce-panel { left: 146px; top: 663px; width: 520px; height: 84px; padding: 10px 14px; }
  .ecommerce-icon { position: absolute; left: 615px; top: 598px; width: 208px; height: 190px; }

  .services-heading { right: 162px; top: 856px; text-align: right; }
  .services-panel { left: 300px; top: 892px; width: 557px; height: 77px; padding: 11px 20px; text-align: right; }
  .services-icon { position: absolute; left: 141px; top: 840px; width: 230px; height: 196px; }
</style>
</head>
<body>
  <header class="site-header">
    <div class="brand">
      <span class="brand-mark"></span>
      <span class="brand-name">Corvatel<br>Solutions</span>
    </div>
    <nav class="main-nav">
      <a href="#">Home</a>
      <a href="#">About</a>
      <a href="#">Services</a>
      <a href="#">Solutions</a>
      <a href="#">Contact</a>
    </nav>
  </header>

  <section class="hero">
    <div class="hero-backdrop" role="img" aria-label="Abstract violet network of data lines over a server room"></div>
    <h1 class="hero-title"><span class="line-one">CORVATEL</span><span class="line-two">SOLUTIONS</span></h1>
    <div class="hero-band">
      <p>Get your business critical data seamlessly integrated into your systems.</p>
      <p>Standardize and enrich data to provide better visibility into sourcing and procurement.</p>
      <p>Solutions to Extract, Analyse, Clean up, Validate and Enrich your data.</p>
    </div>
  </section>

  <h2 class="feature-heading ecommerce-heading">E-COMMERCE DATA CONFIGURATION</h2>
  <div class="feature-panel ecommerce-panel">
    <p>Lorem ipsum dolor sit amet, consectetur adipiscing.<br>In dignissim risus id lorem mattis tristique.</p>
  </div>
  <svg class="ecommerce-icon" viewBox="0 0 208 190" role="img" aria-label="Shopping cart illustration with a check mark">
    <rect x="30" y="30" width="170" height="110" rx="14" fill="var(--cart-orange)" opacity="0.35"/>
    <circle cx="115" cy="50" r="44" fill="var(--cart-dark)" opacity="0.25"/>
    <circle cx="70" cy="165" r="20" fill="var(--cart-dark)" opacity="0.3"/>
    <circle cx="165" cy="165" r="20" fill="var(--cart-dark)" opacity="0.3"/>
  </svg>

  <h2 class="feature-heading services-heading">DATA SERVICES</h2>
  <div class="feature-panel services-panel">
    <p>Data Quality determines the effectiveness<br>of an ERP / PLM / MDM / e-Commerce system</p>
  </div>
  <svg class="services-icon" viewBox="0 0 230 196" role="img" aria-label="Database stack illustration with a gear">
    <rect x="2" y="0" width="172" height="158" rx="40" fill="var(--db-green)" opacity="0.45"/>
    <circle cx="158" cy="126" r="68" fill="var(--gear-violet)" opacity="0.45"/>
  </svg>
</body>
</html>
```